Media Broker Web design

Re-design a website for an independant media buying and planning marketing business in Australia. We develop unique marketing plans for small to medium businesses. NFP's are our sweet spot. We tailor a strategy that takes account of business needs, whilst respecting the brand footprint. Using an innovative and purpose-built media buying platform, we access the best media houses to directly understand availability, and then negotiate the most competitive rates to maximise campaign results and ensure a superior ROI. The current website is not engaging, or very interactive. We are looking at something more inspiring that builds confidence in our business and the work that we do in assisting others to market themselves. We want something clean & simple, engaging, customer centric, easy to navigate, including customer logo's and testimonials. See attached logo and colours - the grey & orange. We ignite brands with performance driven media buying. "You talk, we listen"
Updates

Need extra days to review

Target Market(s)

Companies seeking support with marketing campaigns

Industry/Entity Type

Media

Number of Pages Required

3 page

Colors
F0912C
F2A743
F7CA91
FBE8D2
FDF5EE

Requirements
Must have
• About us, Services offered, contact us, current clients, testimonials
Nice to have
• Team photo

```html
<!DOCTYPE html>
<html lang="en">
<head>
<meta charset="utf-8">
<title>Signal Media Partners</title>
<link href="https://fonts.googleapis.com/css2?family=Lato:wght@700;900&family=Roboto:wght@400;500;700&display=swap" rel="stylesheet">
<style>
:root{
  --orange:#F0912C;
  --orange-2:#F2A743;
  --orange-3:#F7CA91;
  --orange-4:#FBE8D2;
  --cream:#FDF5EE;
  --ink:#3d3d3d;
  --text:#555;
  --grey-bg:#f4f4f4;
  --dark:#333333;
  --white:#fff;
}
*{box-sizing:border-box;margin:0;padding:0}
html,body{width:1200px;height:3416px;overflow:hidden}
body{font-family:"Roboto",Arial,sans-serif;color:var(--text);background:var(--white);position:relative}
section,header,footer{position:absolute;left:0;width:1200px}
.abs{position:absolute}
.btn{position:absolute;display:flex;align-items:center;justify-content:center;background:var(--orange);color:var(--white);font:700 15px "Roboto",sans-serif;border-radius:24px 24px 0 24px;letter-spacing:.2px}
.eyebrow{font:700 22px "Lato",sans-serif;color:var(--orange);text-transform:uppercase;text-align:center;width:100%}
.title{font:700 39px "Lato",sans-serif;color:var(--ink);text-transform:uppercase;text-align:center;width:100%}
.brand{font:500 23px "Roboto",sans-serif;color:var(--ink);display:flex;align-items:center;gap:9px;white-space:nowrap}
.brand .dot{width:18px;height:18px;border-radius:50%;background:var(--orange)}

/* header */
.site-header{top:0;height:137px}
.site-header .brand{left:111px;top:56px}
.nav{position:absolute;top:62px;left:445px;display:flex;gap:46px;font:500 15px "Roboto",sans-serif;color:#222}
.nav .active{color:var(--orange)}
.btn-contact{left:798px;top:47px;width:139px;height:48px}
.btn-phone{left:950px;top:47px;width:138px;height:48px;background:var(--white);color:#222;border:2px solid var(--orange);box-shadow:0 4px 10px rgba(0,0,0,.15)}

/* hero */
.hero{top:137px;height:600px;overflow:hidden}
.hero-visual{position:absolute;inset:0;background:radial-gradient(ellipse at 35% 40%,#8a8a8a 0%,#555 35%,#2e2e2e 75%),#2b2b2b}
.hero-text{position:absolute;left:694px;top:187px;font:700 39px/47px "Lato",sans-serif;color:var(--white);text-transform:uppercase}
.btn-start{left:694px;top:357px;width:150px;height:46px}

/* about */
.about{top:737px;height:622px}
.about .eyebrow{position:absolute;top:110px}
.about .title{position:absolute;top:146px}
.about-copy{position:absolute;top:220px;left:120px;width:960px;text-align:center;font-size:18.5px;line-height:31px;color:#444}
.about-copy p{margin-bottom:16px}
.btn-learn{left:529px;top:473px;width:142px;height:48px}

/* services */
.services{top:1359px;height:593px;background:var(--grey-bg)}
.services .eyebrow{position:absolute;top:68px}
.services .title{position:absolute;top:104px}
.cards{position:absolute;top:181px;left:21px;display:flex;gap:19.5px}
.card{width:275px;height:342px;position:relative;overflow:hidden;color:var(--white)}
.card-label{position:absolute;left:0;right:0;bottom:30px;text-align:center;font:700 17px "Roboto",sans-serif;text-transform:uppercase;text-shadow:0 1px 3px rgba(0,0,0,.5)}
.tv{background:linear-gradient(180deg,#141a28 0%,#26304a 55%,#4a4660 85%,#2a2d3e 100%)}
.ooh{background:linear-gradient(90deg,#7a7873 0%,#a9a7a1 30%,#dcdad5 55%,#c4c2bc 80%,#8e8c86 100%)}
.print{background:var(--orange);text-align:center;padding:50px 26px 0}
.print h3{font:700 18px "Roboto",sans-serif;margin:14px 0 12px}
.print p{font:500 14px/23px "Roboto",sans-serif}
.btn-outline{display:inline-block;margin-top:16px;border:2px solid var(--white);border-radius:16px 16px 0 16px;padding:6px 16px;font:700 11px "Roboto",sans-serif}
.social{background:radial-gradient(ellipse at 50% 62%,#2fb6e8 0%,#1b6a9a 28%,#22304a 60%,#1b2233 100%)}

/* benefits */
.benefits{top:1952px;height:676px}
.benefits-frame{position:absolute;left:111px;top:103px;width:489px;height:445px;border:9px solid var(--orange);border-right:none;border-bottom:none;border-radius:60px 60px 0 60px;overflow:hidden}
.benefits-visual{position:absolute;inset:0;background:radial-gradient(ellipse at 55% 45%,#7a6a52 0%,#4c5560 40%,#2c333b 80%)}
.benefits-copy{position:absolute;left:666px;top:125px;width:423px}
.benefits-copy .eyebrow{font:700 22px "Lato",sans-serif;color:var(--orange);text-align:left;margin:0}
.benefits-copy h2{font:700 30px/36px "Lato",sans-serif;color:var(--ink);text-transform:uppercase;margin:12px 0 20px}
.benefits-copy .body{font-size:15px;line-height:24px;text-align:justify;color:#666;margin-bottom:10px}
.btn-touch{left:666px;top:473px;width:142px;height:48px}

/* testimonials */
.testimonials{top:2628px;height:565px;background:linear-gradient(180deg,var(--orange) 0%,#ec8a24 100%)}
.testimonials .eyebrow{position:absolute;top:75px;color:var(--white)}
.testimonials .title{position:absolute;top:115px;color:var(--white)}
.quotes{position:absolute;top:237px;left:111px;display:flex;gap:21px}
.quote{width:312px;height:245px;background:var(--white);border-radius:18px;border-top:4px solid #444;position:relative;text-align:center;padding:58px 22px 0}
.avatar{position:absolute;left:113px;top:-48px;width:86px;height:86px;border-radius:50%;background:var(--white);border:4px solid #444;display:flex;align-items:center;justify-content:center}
.avatar span{width:30px;height:30px;border-radius:50%;background:var(--orange-3)}
.quote h3{font:700 18.5px "Roboto",sans-serif;color:#333;text-transform:uppercase}
.stars{color:var(--orange);font-size:12px;letter-spacing:1px;margin:4px 0 10px}
.quote p{font-size:13.5px;line-height:24px;color:#555}
.arrow{position:absolute;top:355px}

/* footer */
.site-footer{top:3193px;height:223px;background:var(--dark);color:var(--white)}
.site-footer .brand{position:absolute;left:111px;top:72px;color:var(--white)}
.foot-nav{position:absolute;right:111px;top:78px;display:flex;gap:38px;font:700 15px "Roboto",sans-serif}
.foot-nav .sep{font-weight:400}
.foot-contact{position:absolute;right:111px;top:113px;display:flex;gap:20px;align-items:center;font-size:14px}
.foot-contact span{display:flex;align-items:center;gap:8px}
.rule{position:absolute;left:111px;right:111px;top:162px;height:1px;background:#555}
.copyright{position:absolute;top:187px;width:100%;text-align:center;font-size:12px}
</style>
</head>
<body>

<header class="site-header">
  <div class="brand abs"><span class="dot"></span>Signal Media Partners</div>
  <nav class="nav"><span class="active">HOME</span><span>ABOUT US</span><span>WHAT WE DO</span></nav>
  <div class="btn btn-contact">CONTACT US</div>
  <div class="btn btn-phone">0400 555 019</div>
</header>

<section class="hero">
  <div class="hero-visual" role="img" aria-label="Hand holding a glowing lightbulb with a brain and gears, overlaid with an orange diagonal band"></div>
  <svg class="abs" style="left:0;top:0" width="1200" height="600" aria-hidden="true">
    <polygon points="130,0 380,0 720,600 420,600" fill="#F0912C" opacity=".72"/>
    <polygon points="860,0 1080,0 760,600 540,600" fill="#ffffff" opacity=".08"/>
  </svg>
  <h1 class="hero-text">Independent Media<br>Planning &amp; Buying<br>Specialists</h1>
  <div class="btn btn-start">GET STARTED</div>
</section>

<section class="about">
  <p class="eyebrow">Who we are</p>
  <h2 class="title">Media Planning &amp; Buying Experts</h2>
  <div class="about-copy">
    <p>At Signal Media Partners our motivation is simple - to deliver the greatest impact for your business with the best possible ROI.</p>
    <p>We have the knowledge and expertise to maximise your budget, increase brand awareness and deliver your message in a way that drives people to action.</p>
    <p>SMP's media planning and buying is strategic, innovative, on budget and achieves results. We engage in creative collaboration to deliver a bespoke media plan for your business.</p>
  </div>
  <div class="btn btn-learn">LEARN MORE</div>
</section>

<section class="services">
  <p class="eyebrow">What we do</p>
  <h2 class="title">Our Services</h2>
  <div class="cards">
    <div class="card tv" role="img" aria-label="Broadcast tower with satellite dishes above a city at night"><span class="card-label">Television &amp; Radio</span></div>
    <div class="card ooh" role="img" aria-label="Blank billboard canvas leaning on a concrete wall beside a ladder"><span class="card-label">Out of Home</span></div>
    <div class="card print">
      <svg width="52" height="46" viewBox="0 0 52 46" aria-hidden="true">
        <rect x="13" y="2" width="26" height="12" rx="2" fill="#fff"/>
        <rect x="2" y="16" width="48" height="20" rx="4" fill="#fff"/>
        <rect x="13" y="28" width="26" height="16" rx="2" fill="#fff" stroke="#F0912C" stroke-width="2"/>
        <circle cx="42" cy="23" r="2.5" fill="#F0912C"/>
      </svg>
      <h3>PRINT</h3>
      <p>Print today can still offer good value as part of your media mix. When you are looking to reinforce your media message</p>
      <span class="btn-outline">LEARN MORE</span>
    </div>
    <div class="card social" role="img" aria-label="Hands holding a glowing phone with a network of social reaction icons"><span class="card-label">Digital &amp; Social Media</span></div>
  </div>
</section>

<section class="benefits">
  <div class="benefits-frame">
    <div class="benefits-visual" role="img" aria-label="Person working on a laptop with floating bar charts and a pie chart overlay"></div>
  </div>
  <div class="benefits-copy">
    <p class="eyebrow">Benefits</p>
    <h2>Ready for next level outcomes?</h2>
    <p class="body">Effective media buying requires the coordination of many moving parts, and if done correctly, will increase exposure, build your brand, and grow revenue.</p>
    <p class="body">Using an innovative and purpose-built media buying platform with world-class technology, we access the best media houses to directly understand availability, and then negotiate the most competitive rates to maximise your campaign results and ensure a superior ROI.</p>
  </div>
  <div class="btn btn-touch">GET IN TOUCH</div>
</section>

<section class="testimonials">
  <p class="eyebrow">Testimonials</p>
  <h2 class="title">What our clients say</h2>
  <svg class="arrow" style="left:40px" width="40" height="40" viewBox="0 0 40 40" aria-hidden="true"><circle cx="20" cy="20" r="14" fill="#F7CA91" opacity=".6"/><path d="M24 10 L14 20 L24 30" stroke="#fff" stroke-width="4" fill="none"/></svg>
  <div class="quotes">
    <article class="quote"><div class="avatar"><span></span></div><h3>Media Specialists</h3><div class="stars">★★★★★</div><p>Lorem ipsum dolor sit amet, consectetur adipiscing elit, sed do eiusmod tempor incididunt ut labore et dolore magna aliqua ut enim ad minim veniam, quis nostrud exercitationea.</p></article>
    <article class="quote"><div class="avatar"><span></span></div><h3>Media Specialists</h3><div class="stars">★★★★★</div><p>Lorem ipsum dolor sit amet, consectetur adipiscing elit, sed do eiusmod tempor incididunt ut labore et dolore magna aliqua ut enim ad minim veniam, quis nostrud exercitationea.</p></article>
    <article class="quote"><div class="avatar"><span></span></div><h3>Media Specialists</h3><div class="stars">★★★★★</div><p>Lorem ipsum dolor sit amet, consectetur adipiscing elit, sed do eiusmod tempor incididunt ut labore et dolore magna aliqua ut enim ad minim veniam, quis nostrud exercitationea.</p></article>
  </div>
  <svg class="arrow" style="left:1118px" width="40" height="40" viewBox="0 0 40 40" aria-hidden="true"><circle cx="20" cy="20" r="14" fill="#F7CA91" opacity=".6"/><path d="M16 10 L26 20 L16 30" stroke="#fff" stroke-width="4" fill="none"/></svg>
</section>

<footer class="site-footer">
  <div class="brand"><span class="dot"></span>Signal Media Partners</div>
  <nav class="foot-nav"><span>HOME</span><span class="sep">|</span><span>ABOUT US</span><span class="sep">|</span><span>WHAT WE DO</span><span class="sep">|</span><span>CONTACT US</span></nav>
  <div class="foot-contact">
    <span><svg width="13" height="13" viewBox="0 0 24 24" aria-hidden="true"><path d="M6 2 L10 6 L8 9 C9 12 12 15 15 16 L18 14 L22 18 L19 22 C10 21 3 14 2 5 Z" fill="#F0912C"/></svg>0400 555 019</span>
    <span>|</span>
    <span><svg width="15" height="11" viewBox="0 0 15 11" aria-hidden="true"><rect width="15" height="11" rx="1" fill="#F0912C"/><path d="M0 1 L7.5 6 L15 1" stroke="#333" stroke-width="1.3" fill="none"/></svg>hello@signalmediapartners.com.au</span>
  </div>
  <div class="rule"></div>
  <p class="copyright">© 2024 SIGNAL MEDIA PARTNERS &nbsp;|&nbsp; All Rights Reserved</p>
</footer>

</body>
</html>
```